Premium CBD/Hemp company needs packaging and label design

Verdant Halcyon Labs, a premium CBD/Hemp company based in Scottsdale, Arizona is in need of a packaging and label design. We are launching with our flagship product which will be a 30 count capsule and will come in three functions: Pain Relief, Anxiety Support, and Sleep Support. For the purpose of this contest, please design packaging and label for our Anxiety Support product. Our products are physician formulated and all natural. Our main ingredient is CBD/Hemp and is complemented by specific herbs that synergistically work together to give the customer the most effective and desired result. We would like our branding to have a pharmaceutical look and feel with a focus on trust and transparency. We have uploaded our company logo that is to be used on both the packaging and label. We have also uploaded an executed branding questionnaire that will guide you to exactly what we are seeking to achieve as to the look and feel of our brand. Please feel free to contact us with any questions that you may have. The winner of this contest will have the opportunity to work with us on future projects as we will need packaging and label design for our entire Verdant Halcyon Labs product line.

Target Market(s)

See attached branding questionnaire

Industry/Entity Type

Health And Wellness

Font styles to use
Sans Serif

Colors

Designer to choose colors to be used in the design.

Requirements
Must have
• See attached branding questionnaire; Please superimpose labels onto a cobalt blue capsule bottle (see attached)
• >>UPON REVIEW of the FIRST 8 designs, we really like the silver, mildly metallic label background in DESIGN # 21300528, we do not want metalic lettering as that would not look very "Pharmaceutical"
• >>We are in search of a look that is a bit more "Pharmaceutical" than a look that would be more commonly found in a Supplement Store
Nice to have
• "See attached branding questionnaire
Should not have
• See attached branding questionnaire; NO marijuana or cannabis plant on the packaging or label

```html
<!DOCTYPE html>
<html lang="en">
<head>
<meta charset="utf-8">
<title>Verdant Halcyon Labs – Anxiety Support Label</title>
<link rel="stylesheet" href="https://fonts.googleapis.com/css2?family=Open+Sans:wght@400;600;700;800&family=Oswald:wght@500;600&display=swap">
<style>
  :root {
    --page: #ffffff;
    --silver-light: #fbfbfb;
    --silver-mid: #e4e5e6;
    --silver-dark: #c9cacc;
    --brand-blue: #3340a6;
    --title-grey: #b3b4b6;
    --title-green: #3dbf94;
    --hemp-teal: #2e6f5c;
    --body-grey: #454545;
    --band-dark: #2a9676;
    --band-light: #63caa6;
    --lime: #8fd65a;
    --lime-text: #3f9b34;
    --count-green: #1f6a52;
    --white: #ffffff;
  }
  * { margin: 0; padding: 0; box-sizing: border-box; }
  html, body {
    width: 1200px;
    height: 1164px;
    overflow: hidden;
    background: var(--page);
  }
  .label {
    position: absolute;
    left: 217px;
    top: 118px;
    width: 765px;
    height: 927px;
    font-family: "Open Sans", sans-serif;
    overflow: hidden;
  }
  .label-art {
    position: absolute;
    inset: 0;
    width: 100%;
    height: 100%;
  }
  .brand {
    position: absolute;
    left: 34px;
    top: 72px;
    display: flex;
    align-items: center;
    gap: 18px;
  }
  .brand-mark {
    width: 92px;
    height: 92px;
    border-radius: 50%;
    border: 4px solid var(--brand-blue);
  }
  .brand-name {
    font-size: 40px;
    font-weight: 400;
    color: var(--brand-blue);
    letter-spacing: 1px;
    white-space: nowrap;
  }
  .title {
    position: absolute;
    left: 92px;
    font-size: 114px;
    font-weight: 700;
    letter-spacing: -3px;
    line-height: 1;
  }
  .title-anxiety { top: 278px; color: var(--title-grey); }
  .title-support { top: 384px; color: var(--title-green); }
  .hemp {
    position: absolute;
    left: 140px;
    top: 498px;
    font-size: 36px;
    font-weight: 400;
    letter-spacing: 5px;
    color: var(--hemp-teal);
    line-height: 1;
  }
  .hemp strong { font-weight: 600; }
  .enriched {
    position: absolute;
    left: 144px;
    top: 560px;
    font-size: 33px;
    letter-spacing: -0.8px;
    color: var(--body-grey);
    white-space: nowrap;
  }
  .benefits {
    position: absolute;
    left: 150px;
    top: 636px;
    list-style: none;
  }
  .benefits li {
    position: relative;
    padding-left: 46px;
    font-size: 27px;
    font-weight: 800;
    letter-spacing: 1.5px;
    color: var(--white);
    line-height: 41px;
  }
  .benefits li::before {
    content: "";
    position: absolute;
    left: 2px;
    top: 15px;
    width: 9px;
    height: 9px;
    border-radius: 50%;
    background: var(--white);
  }
  .strength {
    position: absolute;
    right: 17px;
    top: 712px;
    text-align: right;
    color: var(--white);
    transform: rotate(-2deg);
    transform-origin: right bottom;
  }
  .strength-label {
    font-size: 20px;
    font-weight: 700;
    letter-spacing: 1px;
  }
  .strength-value {
    font-family: "Oswald", sans-serif;
    font-size: 44px;
    font-weight: 600;
    line-height: 1.05;
  }
  .strength-value small { font-size: 28px; }
  .ecs {
    position: absolute;
    right: 17px;
    top: 806px;
    font-size: 30px;
    font-weight: 700;
    letter-spacing: -1.6px;
    color: var(--lime-text);
    transform: rotate(-2deg);
    transform-origin: right bottom;
    white-space: nowrap;
  }
  .count {
    position: absolute;
    right: 17px;
    top: 858px;
    font-family: "Oswald", sans-serif;
    font-size: 42px;
    font-weight: 500;
    color: var(--count-green);
    transform: rotate(-3deg);
    transform-origin: right bottom;
    white-space: nowrap;
    line-height: 1;
  }
</style>
</head>
<body>
  <main class="label">
    <svg class="label-art" viewBox="0 0 450 545" preserveAspectRatio="none" aria-hidden="true">
      <defs>
        <linearGradient id="silver" x1="0" y1="0" x2="1" y2="1">
          <stop offset="0" stop-color="var(--silver-light)"/>
          <stop offset="0.45" stop-color="var(--silver-mid)"/>
          <stop offset="0.7" stop-color="var(--silver-light)"/>
          <stop offset="1" stop-color="var(--silver-dark)"/>
        </linearGradient>
        <linearGradient id="band" x1="0" y1="0" x2="1" y2="0">
          <stop offset="0" stop-color="var(--band-dark)"/>
          <stop offset="1" stop-color="var(--band-light)"/>
        </linearGradient>
      </defs>
      <rect class="label-base" width="450" height="545" fill="url(#silver)"/>
      <polygon class="sheen" points="230,0 330,0 450,90 450,170" fill="#ffffff" opacity="0.7"/>
      <polygon class="sheen" points="360,0 400,0 450,40 450,75" fill="#ffffff" opacity="0.8"/>
      <polygon class="side-shade" points="0,290 55,300 55,400 0,405" fill="var(--silver-dark)" opacity="0.6"/>
      <rect class="hemp-bar" x="55" y="292" width="390" height="26" fill="#ffffff" opacity="0.9"/>
      <path class="benefit-band" d="M0,404 C150,384 300,362 450,356 L450,476 L75,498 L30,545 L0,545 Z" fill="url(#band)"/>
      <path class="band-edge" d="M0,404 C150,384 300,362 450,356" fill="none" stroke="var(--lime)" stroke-width="3"/>
      <polygon class="ecs-stripe" points="70,490 450,468 450,497 52,512" fill="var(--lime)"/>
      <polygon class="count-panel" points="30,545 52,512 450,497 450,545" fill="#ffffff"/>
    </svg>

    <div class="brand">
      <span class="brand-mark"></span>
      <span class="brand-name">Verdant Halcyon Labs</span>
    </div>

    <h1 class="title title-anxiety">ANXIETY</h1>
    <h2 class="title title-support">SUPPORT</h2>

    <p class="hemp">HEMP <strong>EXTRACT</strong></p>
    <p class="enriched">Enriched with Special Herbal Mixture</p>

    <ul class="benefits">
      <li>PAIN RELIEF</li>
      <li>ANXIETY RELIEF</li>
      <li>SLEEP SUPPORT</li>
      <li>WELL.BEING</li>
    </ul>

    <div class="strength">
      <div class="strength-label">STRENGTH</div>
      <div class="strength-value">20<small>MG</small>/CAPSULE</div>
    </div>

    <p class="ecs">ENDOCANNABINOID SYSTEM SUPPORT</p>
    <p class="count">30 GEL CAPSULES</p>
  </main>
</body>
</html>
```